LEARN Business Skills so you can Earn a good living

size of the poster is 8”x 10.75" plus 0.25" bleed.
Please leave 1 inch on the bottoum for footer
I want a design a poster that will attract people's attention.
I appreciate a creative ad however the ad should not take away from being able to clearly read the text.
-I also appreciate a simple creative ad that is not too busy.
-you can use graphics, vectors, or pictures of real people.
-however, if you use real people it should be a white male that is wearing a white shirt and look like a professional person.

Target Market(s)

Potential young business people

Industry/Entity Type

education

Requirements
Must have
• easy to read the text
Nice to have
• I would like a "creative" simple ad that is easy to be read
Should not have
• pictures of women

```html
<!DOCTYPE html>
<html lang="en">
<head>
<meta charset="utf-8">
<title>Learn It to Earn It – Business Enrichment Course</title>
<link href="https://fonts.googleapis.com/css2?family=League+Gothic&family=Montserrat:wght@200&family=Lato:wght@400&family=Oswald:wght@600&display=swap" rel="stylesheet">
<style>
  :root {
    --teal: #5cfddc;
    --yellow: #fdc82d;
    --white: #ffffff;
    --ink: #151515;
    --pill: #c4cfca;
    --bar-grey: #c8cfcc;
    --photo-light: #eef0ef;
    --photo-mid: #bfc3c1;
    --photo-dark: #9da29f;
  }
  * { margin: 0; padding: 0; box-sizing: border-box; }
  html, body { width: 893px; height: 1200px; overflow: hidden; background: var(--white); }
  .poster { position: relative; width: 893px; height: 1200px; overflow: hidden; background: var(--white); }

  .hero { position: absolute; left: 0; top: 0; width: 893px; height: 620px; background: var(--teal); overflow: hidden; }
  .accent-bar { position: absolute; left: 784px; top: 0; width: 48px; height: 373px; background: var(--yellow); }
  .hero-photo {
    position: absolute; left: 389px; top: 124px; width: 504px; height: 496px;
    border-radius: 220px 220px 0 0;
    background: radial-gradient(ellipse at 62% 28%, var(--photo-light) 0%, var(--photo-light) 28%, var(--photo-mid) 55%, var(--photo-dark) 100%);
  }

  .headline {
    position: absolute; left: 110px; top: 100px;
    font-family: "League Gothic", "Oswald", sans-serif; font-weight: 400;
    font-size: 104px; line-height: 1; letter-spacing: 0; color: var(--white); white-space: nowrap;
  }
  .headline .earn { color: var(--yellow); }

  .course-title {
    position: absolute; left: 110px; top: 258px;
    font-family: "Montserrat", sans-serif; font-weight: 200;
    font-size: 52px; line-height: 67px; color: var(--white);
  }

  .proof { position: absolute; left: 113px; top: 523px; width: 630px; height: 45px; border-radius: 8px; background: rgba(255,255,255,0.78); }
  .proof-tick { position: absolute; left: 88px; top: 529px; width: 46px; height: 32px; }
  .proof-text {
    position: absolute; left: 153px; top: 531px;
    font-family: "Lato", sans-serif; font-size: 22px; line-height: 30px; color: var(--ink); white-space: nowrap;
  }

  .skills-heading {
    position: absolute; left: 111px; top: 676px;
    font-family: "Oswald", sans-serif; font-weight: 600; font-size: 34px; line-height: 44px;
    color: var(--ink); letter-spacing: 1.8px; white-space: nowrap;
  }

  .benefits { position: absolute; left: 111px; top: 758px; list-style: none; }
  .benefits li {
    position: relative; padding-left: 23px; height: 37px;
    font-family: "Lato", sans-serif; font-size: 35px; line-height: 37px; color: var(--ink); white-space: nowrap;
  }
  .benefits li::before { content: ""; position: absolute; left: 0; top: 5px; width: 12px; height: 28px; }
  .benefits .job::before { background: var(--yellow); }
  .benefits .business::before { background: var(--bar-grey); }
  .benefits .salary::before { background: var(--teal); }

  .topics { position: absolute; left: 0; top: 0; width: 893px; height: 1200px; list-style: none; pointer-events: none; }
  .topic {
    position: absolute; height: 31px; border-radius: 16px; background: var(--pill);
    font-family: "Lato", sans-serif; font-size: 16.5px; line-height: 31px; color: var(--ink);
    text-align: center; white-space: nowrap;
  }
  .row-1 { top: 925px; }
  .row-2 { top: 970px; }
  .row-3 { top: 1015px; }
  .row-4 { top: 1060px; }
</style>
</head>
<body>
<main class="poster">
  <section class="hero">
    <div class="accent-bar"></div>
    <div class="hero-photo" role="img" aria-label="Photo of a smiling young professional man in glasses, a white shirt and a light grey blazer"></div>
    <h1 class="headline">LEARN IT to <span class="earn">EARN IT</span></h1>
    <p class="course-title">Business<br>Enrichment<br>Course</p>
    <div class="proof"></div>
    <svg class="proof-tick" viewBox="0 0 46 32" aria-hidden="true">
      <polyline points="5,17 17,27 41,5" fill="none" stroke="#fdc82d" stroke-width="9" stroke-linejoin="miter"/>
    </svg>
    <p class="proof-text">A proven success of helping people in their livelihoods</p>
  </section>

  <h2 class="skills-heading">BUSINESS SKILLS THAT WILL HELP YOU:</h2>

  <ul class="benefits">
    <li class="job">Get a quality job</li>
    <li class="business">Start/grow your business</li>
    <li class="salary">Increase your salary</li>
  </ul>

  <ul class="topics">
    <li class="topic row-1" style="left:112px;width:204px">business administration</li>
    <li class="topic row-1" style="left:327px;width:237px">small business management</li>
    <li class="topic row-1" style="left:577px;width:77px">finance</li>
    <li class="topic row-1" style="left:668px;width:110px">investments</li>

    <li class="topic row-2" style="left:112px;width:95px">computers</li>
    <li class="topic row-2" style="left:216px;width:94px">accounting</li>
    <li class="topic row-2" style="left:320px;width:50px">sales</li>
    <li class="topic row-2" style="left:378px;width:96px">marketing</li>
    <li class="topic row-2" style="left:483px;width:110px">business law</li>
    <li class="topic row-2" style="left:599px;width:98px">negotiation</li>
    <li class="topic row-2" style="left:707px;width:71px">retail</li>

    <li class="topic row-3" style="left:112px;width:303px">project management interviewing skills</li>
    <li class="topic row-3" style="left:422px;width:123px">public speaking</li>
    <li class="topic row-3" style="left:550px;width:119px">import/export</li>
    <li class="topic row-3" style="left:676px;width:105px">health care</li>

    <li class="topic row-4" style="left:112px;width:106px">distribution</li>
    <li class="topic row-4" style="left:227px;width:192px">information technology</li>
    <li class="topic row-4" style="left:427px;width:115px">bookkeeping</li>
    <li class="topic row-4" style="left:550px;width:107px">real estate</li>
    <li class="topic row-4" style="left:671px;width:107px">management</li>
  </ul>
</main>
</body>
</html>
```